Design a Call-To-Action Card

We need the following:

* An attractive card design in PSD format which we will print on PVC Plastic Card (CR80 Stock)
* Our logo somewhere on the card
* Our main colours are blue (#24b8dc) and white
* A title stating: "Kelvane Fibre internet is coming"
* Our website, www.mv.kel.nz/joinnow

This card is going to be a call-to-action, in which we would like people to visit our site to purchase our product. The card must look eye catching and professional. If you think it will look good, feel free to add elements such as QR codes.

Best entry will be awarded and we will get this freelancer to create a few more cards (business cards and other call to action cards) for us.

```html
<!DOCTYPE html>
<html lang="en">
<head>
<meta charset="utf-8">
<title>Kelvane Fibre – Call-To-Action Card</title>
<link rel="stylesheet" href="https://fonts.googleapis.com/css2?family=Open+Sans:wght@400;700&display=swap">
<style>
  :root {
    --backdrop: #2b2b2b;
    --card-dark-top: #3d3d3d;
    --card-dark-bottom: #1c1c1c;
    --brand-blue: #24b8dc;
    --teal-deep: #1d2427;
    --teal-light: #1f7f93;
    --text-light: #ffffff;
    --text-soft: #cfcfcf;
  }
  * { margin: 0; padding: 0; box-sizing: border-box; }
  html, body {
    width: 1200px;
    height: 600px;
    overflow: hidden;
    background: var(--backdrop);
    font-family: "Open Sans", Arial, sans-serif;
  }
  .canvas {
    width: 1200px;
    height: 600px;
    display: flex;
    align-items: center;
    justify-content: center;
    gap: 60px;
  }
  .card {
    width: 500px;
    height: 315px;
    border-radius: 6px;
    box-shadow: 0 10px 30px rgba(0, 0, 0, 0.45);
    position: relative;
    overflow: hidden;
  }
  .card-front {
    background: linear-gradient(160deg, var(--card-dark-top) 0%, var(--card-dark-bottom) 100%);
    display: flex;
    flex-direction: column;
    align-items: center;
    justify-content: center;
  }
  .brand {
    display: flex;
    align-items: center;
    gap: 14px;
    margin-bottom: 42px;
  }
  .brand-dot {
    width: 40px;
    height: 40px;
    border-radius: 50%;
    background: var(--brand-blue);
  }
  .brand-name {
    font-size: 40px;
    font-weight: 700;
    color: var(--brand-blue);
    letter-spacing: 0.5px;
  }
  .headline {
    text-align: center;
    color: var(--text-light);
  }
  .headline-main {
    font-size: 24px;
    font-weight: 700;
    line-height: 1.1;
  }
  .headline-sub {
    font-size: 15px;
    font-weight: 400;
    color: var(--text-soft);
    margin-top: 2px;
  }
  .card-back {
    background: linear-gradient(90deg, var(--teal-deep) 0%, var(--teal-light) 100%);
    display: flex;
    align-items: center;
    justify-content: center;
  }
  .web-address {
    font-size: 17px;
    font-weight: 700;
    color: var(--text-light);
    letter-spacing: 0.2px;
  }
</style>
</head>
<body>
  <main class="canvas">
    <section class="card card-front">
      <div class="brand">
        <span class="brand-dot"></span>
        <span class="brand-name">Kelvane</span>
      </div>
      <div class="headline">
        <p class="headline-main">Kelvane Fibre internet</p>
        <p class="headline-sub">is coming</p>
      </div>
    </section>
    <section class="card card-back">
      <p class="web-address">www.mv.kel.nz/joinnow</p>
    </section>
  </main>
</body>
</html>
```